A-Stand Directional Sign Design

Objective:
We need a professional graphic design for an A-Stand sign that will guide customers arriving in our parking lot to our office. The design should be visually clear, welcoming, and aligned with our brand identity.
REQUIREMENTS:
Two versions of the design:
- One with an arrow pointing left
- One with an arrow pointing right
(This allows us to place the A-Stand anywhere and flip the graphic as needed.)
DIMENSIONS:
- Viewable Area: 30" x 40"
BRAND ALIGNMENT:
- Colors, fonts, and overall style should match our website: www.skornabel.com
- Clean, modern, and professional look consistent with our aviation/tourism brand
CONTENT:
- Clear directional arrow (left or right depending on version)
- Text: “Office Entrance” or similar concise wording (designers may propose alternatives if they improve clarity)
READABILITY:
- Bold, high-contrast design for visibility from a distance
- Simple layout that avoids clutter
DELIVERABLES:
- Final artwork in print-ready format (PDF preferred)
- Two versions: Arrow Left and Arrow Right
DESIGN GOAL:
Ensure customers can easily find our office upon arrival, while reinforcing skorNABEL’s professional and welcoming brand image.
Target Market(s)
Tourism

```html
<!DOCTYPE html>
<html lang="en">
<head>
<meta charset="utf-8">
<title>skorNABEL – Office Entrance A-Stand Signs</title>
<link rel="stylesheet" href="https://fonts.googleapis.com/css2?family=Roboto+Condensed:wght@700&family=Montserrat:wght@500&display=swap">
<style>
  :root {
    --backdrop: #f1f0f1;
    --brand-blue: #2150a5;
    --brand-blue-deep: #1c4596;
    --brand-blue-light: #4a72b8;
    --sign-white: #ffffff;
  }
  * { margin: 0; padding: 0; box-sizing: border-box; }
  html, body {
    width: 1200px;
    height: 2561px;
    overflow: hidden;
    background: var(--backdrop);
  }
  .sign-sheet {
    display: grid;
    grid-template-rows: 1280px 1281px;
    width: 1200px;
    height: 2561px;
  }
  .sign-version {
    position: relative;
    display: flex;
    align-items: center;
    justify-content: center;
  }
  .sign-panel {
    position: relative;
    width: 870px;
    height: 1160px;
    background: var(--brand-blue);
    overflow: hidden;
  }
  .sign-panel__backdrop {
    position: absolute;
    inset: 0;
    background:
      radial-gradient(ellipse at 85% 8%, rgba(120,150,205,0.55), transparent 45%),
      linear-gradient(160deg, var(--brand-blue) 0%, var(--brand-blue-deep) 60%, var(--brand-blue) 100%);
  }
  .sign-panel__rule {
    position: absolute;
    inset: 44px 46px;
    border: 3px solid var(--sign-white);
  }
  .brand-name {
    position: absolute;
    top: 150px;
    left: 0;
    right: 0;
    text-align: center;
    font-family: "Montserrat", sans-serif;
    font-weight: 500;
    font-size: 40px;
    letter-spacing: 1px;
    color: var(--sign-white);
  }
  .sign-heading {
    position: absolute;
    top: 285px;
    left: 0;
    right: 0;
    text-align: center;
    font-family: "Roboto Condensed", sans-serif;
    font-weight: 700;
    color: var(--sign-white);
    text-transform: uppercase;
    line-height: 1;
  }
  .sign-heading__line {
    display: block;
    font-size: 170px;
    letter-spacing: -3px;
  }
  .sign-heading__line + .sign-heading__line { margin-top: 30px; }
  .direction-arrow {
    position: absolute;
    top: 690px;
    left: 50%;
    width: 446px;
    height: 380px;
    margin-left: -223px;
  }
  .direction-arrow--left { transform: scaleX(-1); }
</style>
</head>
<body>
<main class="sign-sheet">

  <section class="sign-version sign-version--right" aria-label="Arrow right version">
    <div class="sign-panel">
      <div class="sign-panel__backdrop" role="img" aria-label="Faint blue-toned photograph of a helicopter behind the sign text"></div>
      <div class="sign-panel__rule"></div>
      <p class="brand-name">skorNABEL</p>
      <h1 class="sign-heading">
        <span class="sign-heading__line">Office</span>
        <span class="sign-heading__line">Entrance</span>
      </h1>
      <svg class="direction-arrow direction-arrow--right" viewBox="0 0 260 222" aria-label="Arrow pointing right" role="img">
        <polygon fill="#ffffff" points="0,78 165,78 105,0 175,0 260,111 175,222 105,222 165,144 0,144"/>
      </svg>
    </div>
  </section>

  <section class="sign-version sign-version--left" aria-label="Arrow left version">
    <div class="sign-panel">
      <div class="sign-panel__backdrop" role="img" aria-label="Faint blue-toned photograph of a helicopter behind the sign text"></div>
      <div class="sign-panel__rule"></div>
      <p class="brand-name">skorNABEL</p>
      <h1 class="sign-heading">
        <span class="sign-heading__line">Office</span>
        <span class="sign-heading__line">Entrance</span>
      </h1>
      <svg class="direction-arrow direction-arrow--left" viewBox="0 0 260 222" aria-label="Arrow pointing left" role="img">
        <polygon fill="#ffffff" points="0,78 165,78 105,0 175,0 260,111 175,222 105,222 165,144 0,144"/>
      </svg>
    </div>
  </section>

</main>
</body>
</html>
```